CoralPathway background design

The task is to create a modern looking and very attractive background for the coralPathway laboratory results reports + cover-page for the reports that matches the same design.

The background should be beautiful but also minimalistic enough not to interfere with the content inside the reports. If the background behind the content is too intensive then it is difficult to read the content. Our LOGO is blue and we have used blue-ish colors so far so perhaps one should try to keep blue at least as one of the colors. We have preferred to keep the design abstract/minimalistic rather than using photos.

Please look at the attached files, especially the file "Report with the current background" where you will see how the content is layed inside the reports. You will also see the current background that we would like to change. Then there is a file that contains the report pages without background that you could use to present the background.

```html
<!DOCTYPE html>
<html lang="en">
<head>
<meta charset="utf-8">
<title>CoralPathway – Laboratory Test Results</title>
<link href="https://fonts.googleapis.com/css2?family=Arimo:wght@400;700&display=swap" rel="stylesheet">
<style>
  :root {
    --backdrop: #d9d9db;
    --paper: #ffffff;
    --brand-blue: #29aae1;
    --ink: #3c3c3c;
    --ink-soft: #4a4a4a;
    --wash: rgba(185, 205, 230, 0.45);
    --wash-deep: rgba(160, 180, 220, 0.35);
    --bar-red: #e53b2c;
    --bar-yellow: #f2c51c;
    --bar-green: #48b649;
    --pin: #7a7a7a;
  }
  * { box-sizing: border-box; margin: 0; padding: 0; }
  html, body { width: 999px; height: 1200px; overflow: hidden; }
  body {
    background: var(--backdrop);
    font-family: "Arimo", Arial, sans-serif;
    color: var(--ink);
    position: relative;
  }
  .report-page {
    position: absolute;
    left: 70px; top: 20px;
    width: 860px; height: 1160px;
    background: var(--paper);
    overflow: hidden;
  }
  .corner-wash { position: absolute; pointer-events: none; }
  .corner-wash.top-left {
    left: 0; top: 0; width: 320px; height: 200px;
    background: radial-gradient(ellipse at 0% 0%, var(--wash), rgba(255,255,255,0) 70%);
  }
  .corner-wash.bottom-left {
    left: 0; bottom: 0; width: 460px; height: 240px;
    background: radial-gradient(ellipse at 0% 100%, var(--wash), rgba(255,255,255,0) 70%);
  }
  .corner-wash.bottom-right {
    right: 0; bottom: 0; width: 440px; height: 420px;
    background: radial-gradient(ellipse at 100% 90%, var(--wash-deep), rgba(255,255,255,0) 70%);
  }
  .brand {
    position: absolute; left: 566px; top: 66px;
    display: flex; align-items: center; gap: 12px;
  }
  .brand-dot { width: 44px; height: 44px; border-radius: 50%; background: var(--brand-blue); }
  .brand-name { font-size: 27px; font-weight: 400; color: var(--brand-blue); letter-spacing: -0.3px; }
  .report-title {
    position: absolute; left: 61px; top: 190px;
    font-size: 25px; font-weight: 400; color: var(--brand-blue); letter-spacing: 0.3px;
  }
  .metric { position: absolute; width: 340px; }
  .metric-head { display: flex; justify-content: space-between; align-items: baseline; height: 20px; }
  .metric-name { font-size: 14.5px; font-weight: 700; color: var(--ink); }
  .metric-value { font-size: 12px; font-weight: 700; color: var(--ink); }
  .metric-value sup { font-size: 9px; margin-left: 6px; }
  .scale { position: relative; margin-top: 22px; height: 6px; border-radius: 3px; }
  .scale::before, .scale::after {
    content: ""; position: absolute; top: 0; width: 2px; height: 6px; background: var(--paper);
  }
  .scale::before { left: 33.3%; }
  .scale::after { left: 66.6%; }
  .scale-full { background: linear-gradient(90deg, var(--bar-red), var(--bar-yellow) 25%, var(--bar-green) 50%, var(--bar-yellow) 75%, var(--bar-red)); }
  .scale-rising { background: linear-gradient(90deg, var(--bar-green), var(--bar-green) 25%, var(--bar-yellow) 62%, var(--bar-red)); }
  .scale-falling { background: linear-gradient(90deg, var(--bar-red), var(--bar-yellow) 38%, var(--bar-green) 75%, var(--bar-green)); }
  .pin { position: absolute; top: -22px; width: 14px; height: 20px; transform: translateX(-7px); }
  .scale-labels { display: flex; justify-content: space-between; margin-top: 9px; font-size: 12px; color: var(--ink-soft); }
  .metric-note { margin-top: 13px; font-size: 12.4px; line-height: 18px; color: var(--ink-soft); }
  .metric-note.justified { text-align: justify; }
  .col-left { left: 61px; }
  .col-right { left: 452px; }
  .row-1 { top: 258px; }
  .row-2 { top: 503px; }
  .row-3 { top: 748px; }
</style>
</head>
<body>
<main class="report-page">
  <div class="corner-wash top-left" role="img" aria-label="Soft blue abstract sweep decoration in the top-left corner"></div>
  <div class="corner-wash bottom-left" role="img" aria-label="Soft blue abstract sweep decoration in the bottom-left corner"></div>
  <div class="corner-wash bottom-right" role="img" aria-label="Soft blue and grey abstract sweep with halftone texture in the bottom-right corner"></div>

  <div class="brand">
    <span class="brand-dot"></span>
    <span class="brand-name">CoralPathway</span>
  </div>

  <h1 class="report-title">LABORATORY TEST RESULTS</h1>

  <section class="metric col-left row-1">
    <div class="metric-head"><span class="metric-name">Glucose</span><span class="metric-value">78 mg/dl</span></div>
    <div class="scale scale-full"><svg class="pin" style="left:50%" viewBox="0 0 14 20"><path d="M7 19 C3 12 1.5 9.5 1.5 7 A5.5 5.5 0 0 1 12.5 7 C12.5 9.5 11 12 7 19Z" fill="#fff" stroke="var(--pin)" stroke-width="1.4"/><circle cx="7" cy="7" r="2" fill="none" stroke="var(--pin)" stroke-width="1.2"/></svg></div>
    <div class="scale-labels"><span>low</span><span>normal 60-99</span><span>high</span></div>
    <p class="metric-note">Glucose is the main source of energy for the body. The danger of continuously high blood glucose is that sugar coats the red blood cells, causing them to become stiff and "sticky". These cells interfere with proper blood circulation and cause build-up on blood vessels. High blood sugar can lead to cardiovascular and kidney disease, blindness, or ulcers.</p>
  </section>

  <section class="metric col-right row-1">
    <div class="metric-head"><span class="metric-name">C-reactive protein</span><span class="metric-value">1.2 mg/l</span></div>
    <div class="scale scale-rising"><svg class="pin" style="left:7.5%" viewBox="0 0 14 20"><path d="M7 19 C3 12 1.5 9.5 1.5 7 A5.5 5.5 0 0 1 12.5 7 C12.5 9.5 11 12 7 19Z" fill="#fff" stroke="var(--pin)" stroke-width="1.4"/><circle cx="7" cy="7" r="2" fill="none" stroke="var(--pin)" stroke-width="1.2"/></svg></div>
    <div class="scale-labels"><span>normal ≤5</span><span>high</span></div>
    <p class="metric-note">C-reactive protein (CRP) is a general inflammation marker. Any tissue injury or infection will raise the amount of CRP in the blood within a few hours. After the inflammation is gone, CRP goes down fast. Increased CRP levels not related to acute illness or infection have been linked to higher risk of heart disease.</p>
  </section>

  <section class="metric col-left row-2">
    <div class="metric-head"><span class="metric-name">Sodium</span><span class="metric-value">142 mmol/l</span></div>
    <div class="scale scale-full"><svg class="pin" style="left:56%" viewBox="0 0 14 20"><path d="M7 19 C3 12 1.5 9.5 1.5 7 A5.5 5.5 0 0 1 12.5 7 C12.5 9.5 11 12 7 19Z" fill="#fff" stroke="var(--pin)" stroke-width="1.4"/><circle cx="7" cy="7" r="2" fill="none" stroke="var(--pin)" stroke-width="1.2"/></svg></div>
    <div class="scale-labels"><span>low</span><span>normal 136-146</span><span>high</span></div>
    <p class="metric-note">The amount of sodium is closely related to the amount of water in the body. Excess levels may occur in dehydration, excess sodium in your diet or several diseases. Low levels may occur in cases of heart failure, severe sweating, diarrhea or vomiting, poor nutrition or drinking too much water.</p>
  </section>

  <section class="metric col-right row-2">
    <div class="metric-head"><span class="metric-name">Potassium</span><span class="metric-value">5.2 mmol/l</span></div>
    <div class="scale scale-full"><svg class="pin" style="left:72%" viewBox="0 0 14 20"><path d="M7 19 C3 12 1.5 9.5 1.5 7 A5.5 5.5 0 0 1 12.5 7 C12.5 9.5 11 12 7 19Z" fill="#fff" stroke="var(--pin)" stroke-width="1.4"/><circle cx="7" cy="7" r="2" fill="none" stroke="var(--pin)" stroke-width="1.2"/></svg></div>
    <div class="scale-labels"><span>low</span><span>normal 3.5-5.1</span><span>high</span></div>
    <p class="metric-note justified">Potassium helps nerves and muscles communicate. Dehydration, diarrhea, and excessive sweating are common causes of low potassium levels. Changes in potassium level alter the activity of nerves and muscles, especially the heart: low levels can lead to an irregular heartbeat and high levels cause decreased heart muscle activity.</p>
  </section>

  <section class="metric col-left row-3">
    <div class="metric-head"><span class="metric-name">Creatinine</span><span class="metric-value">1.1 mg/dl</span></div>
    <div class="scale scale-full"><svg class="pin" style="left:63%" viewBox="0 0 14 20"><path d="M7 19 C3 12 1.5 9.5 1.5 7 A5.5 5.5 0 0 1 12.5 7 C12.5 9.5 11 12 7 19Z" fill="#fff" stroke="var(--pin)" stroke-width="1.4"/><circle cx="7" cy="7" r="2" fill="none" stroke="var(--pin)" stroke-width="1.2"/></svg></div>
    <div class="scale-labels"><span>low</span><span>normal 0.7-1.2</span><span>high</span></div>
    <p class="metric-note justified">Creatinine is critical for evaluating renal function. Your serum creatinine is a waste product that is formed when muscle cells break down in your blood. It is produced by muscles as it depends on muscle mass and protein intake. High levels could indicate kidney dysfunction while decreased levels may reflect low muscle mass.</p>
  </section>

  <section class="metric col-right row-3">
    <div class="metric-head"><span class="metric-name">EGFR</span><span class="metric-value">98 ml/min/1.73 m<sup>2</sup></span></div>
    <div class="scale scale-falling"><svg class="pin" style="left:83%" viewBox="0 0 14 20"><path d="M7 19 C3 12 1.5 9.5 1.5 7 A5.5 5.5 0 0 1 12.5 7 C12.5 9.5 11 12 7 19Z" fill="#fff" stroke="var(--pin)" stroke-width="1.4"/><circle cx="7" cy="7" r="2" fill="none" stroke="var(--pin)" stroke-width="1.2"/></svg></div>
    <div class="scale-labels"><span>low</span><span>normal &gt;60</span></div>
    <p class="metric-note">An estimated glomerular filtration rate (eGFR) is calculated according to your creatinine level, age, sex and race. The eGFR is used to screen for and detect early kidney damage and to monitor kidney status. An eGFR below 60 mL/min suggests that some kidney damage has occurred.</p>
  </section>
</main>
</body>
</html>
```